Landing page for car servicing company - Web design

Create a modern looking landing page with the goal to maximise bookings. A booking is made when a customer fills in the form and click on the button "Get Quote".

Important features, that we prefer you do not change too much:
1. Conversion field and call to action.
2. Logotype, it may be turned white on a dark background. Our blue color is #51a0d6.
3. Automotive theme
4. Please use our 60% off badge if possible: [url removed, login to view]

Sites we like and why:
[url removed, login to view] - Conversion focus, Few distractions, Modern design
http:// [url removed, login to view] - Conversion focus, Attention grabbing, Modern
[url removed, login to view] - Conversion focused, Product focused, Modern

Reward for winner beyond money:
The winner will be required to provide a layered PSD file (or something equivalent). We are looking for long-term freelance consultants, so winning the price is only the first reward.

What we will evaluate:
1. The landing page web design should focus on above-fold, what is visible without scrolling on a PC.
2. The website also needs to be able to work on a mobile.
3. Things below fold are not important, and will not be taken into account when selecting the winner.

Process:
- Please ask any questions.
- We will seal the competition after three days.
- Getting feedback from us will increase your chances to win the competition, so post your contribution as soon as possible.

```html
<!DOCTYPE html>
<html lang="en">
<head>
<meta charset="utf-8">
<title>tunebay – Car Servicing</title>
<link href="https://fonts.googleapis.com/css2?family=Lato:ital,wght@0,400;0,700;0,900;1,400;1,700&display=swap" rel="stylesheet">
<style>
  :root {
    --brand-blue: #51a0d6;
    --white: #ffffff;
    --field-text: #9aa3ad;
    --field-line: #e3e7eb;
    --press-grey: rgba(210, 218, 226, 0.45);
    --hero-dark: #101820;
    --hero-mid: #2a3644;
    --hero-steel: #4a5662;
  }
  * { box-sizing: border-box; margin: 0; padding: 0; }
  html, body { width: 1200px; height: 592px; overflow: hidden; }
  body { font-family: 'Lato', sans-serif; color: var(--white); background: var(--hero-dark); }

  .landing { position: relative; width: 1200px; height: 592px; overflow: hidden; }

  .hero-photo {
    position: absolute; inset: 0;
    background:
      radial-gradient(ellipse 420px 300px at 880px 160px, rgba(110,120,130,0.55), transparent 70%),
      radial-gradient(ellipse 500px 260px at 650px 460px, rgba(90,100,112,0.55), transparent 70%),
      radial-gradient(ellipse 300px 200px at 1060px 330px, rgba(120,40,40,0.35), transparent 70%),
      linear-gradient(180deg, var(--hero-mid) 0%, var(--hero-steel) 45%, var(--hero-mid) 75%, var(--hero-dark) 100%);
  }
  .hero-shade { position: absolute; inset: 0; background: linear-gradient(90deg, rgba(10,16,24,0.55) 0%, rgba(10,16,24,0.15) 70%, rgba(10,16,24,0.05) 100%); }

  .site-logo { position: absolute; left: 236px; top: 28px; display: flex; align-items: center; gap: 8px; }
  .site-logo .mark { width: 18px; height: 18px; border-radius: 50%; background: var(--white); }
  .site-logo .name { font-size: 19px; font-weight: 700; color: var(--white); letter-spacing: -0.2px; }

  .main-nav { position: absolute; top: 31px; left: 0; width: 1200px; font-size: 12px; font-weight: 700; letter-spacing: 0.2px; }
  .main-nav a { position: absolute; top: 0; color: var(--white); text-decoration: none; white-space: nowrap; }
  .main-nav .nav-how { left: 612px; }
  .main-nav .nav-repairs { left: 721px; }
  .main-nav .nav-contact { left: 789px; }
  .main-nav .phone { left: 880px; display: flex; align-items: center; gap: 6px; }

  .headline { position: absolute; left: 232px; top: 160px; font-size: 44px; font-weight: 700; line-height: 54px; letter-spacing: 1.5px; text-transform: uppercase; white-space: nowrap; }
  .subline { position: absolute; left: 233px; top: 284px; font-size: 20px; font-style: italic; letter-spacing: 1px; white-space: nowrap; }

  .quote-form { position: absolute; left: 233px; top: 333px; width: 544px; height: 30px; display: flex; }
  .quote-field { background: var(--white); display: flex; align-items: center; gap: 10px; padding-left: 12px; width: 189px; color: var(--field-text); font-size: 11px; }
  .quote-field + .quote-field { border-left: 1px solid var(--field-line); }
  .quote-field .gb { width: 14px; height: 14px; border: 1px solid var(--field-text); border-radius: 50%; font-size: 6px; display: flex; align-items: center; justify-content: center; }
  .quote-button { width: 166px; border: 0; background: var(--brand-blue); color: var(--white); font: 700 12px 'Lato', sans-serif; letter-spacing: 0.4px; }
  .reg-help { position: absolute; left: 233px; top: 373px; font-size: 10.5px; color: var(--white); text-decoration: underline; }

  .discount-badge { position: absolute; left: 883px; top: 177px; width: 93px; height: 93px; border-radius: 50%; background: var(--white); color: var(--brand-blue); text-align: center; font-weight: 700; }
  .discount-badge .small { display: block; font-size: 12px; margin-top: 14px; }
  .discount-badge .big { display: block; font-size: 32px; line-height: 32px; font-weight: 900; }
  .discount-badge .off { display: block; font-size: 16px; line-height: 18px; }
  .discount-note { position: absolute; left: 869px; top: 277px; width: 120px; text-align: center; font-size: 10.5px; line-height: 14px; text-decoration: underline; }

  .hero-links { position: absolute; top: 424px; left: 0; width: 1200px; }
  .video-link { position: absolute; display: flex; align-items: center; gap: 10px; font-size: 12px; font-weight: 700; letter-spacing: 0.3px; top: 12px; white-space: nowrap; }
  .video-link.how { left: 344px; }
  .video-link.pitch { left: 737px; }
  .play { width: 23px; height: 23px; border-radius: 50%; background: var(--white); display: flex; align-items: center; justify-content: center; }

  .rating { position: absolute; left: 523px; width: 160px; text-align: center; }
  .rating .label { font-size: 11px; }
  .rating .stars { display: flex; justify-content: center; gap: 3px; margin: 4px 0 3px; }
  .rating .score { font-size: 10px; }
  .rating .more { font-size: 10px; text-decoration: underline; display: block; margin-top: 3px; }

  .press-row { position: absolute; top: 530px; left: 233px; display: flex; align-items: center; }
  .press-row .label { font-size: 11px; font-style: italic; margin-right: 32px; white-space: nowrap; }
  .press-badges { display: flex; align-items: center; gap: 32px; }
  .press-badge { background: var(--press-grey); height: 12px; border-radius: 2px; }
  .press-badge.round { border-radius: 50%; height: 22px; width: 22px; }
</style>
</head>
<body>
<main class="landing">
  <div class="hero-photo" role="img" aria-label="Mechanic leaning over an open car engine in a workshop"></div>
  <div class="hero-shade"></div>

  <header>
    <div class="site-logo"><span class="mark"></span><span class="name">tunebay</span></div>
    <nav class="main-nav">
      <a href="#" class="nav-how">HOW IT WORKS</a>
      <a href="#" class="nav-repairs">REPAIRS</a>
      <a href="#" class="nav-contact">CONTACT US</a>
      <a href="#" class="phone">
        <svg width="11" height="11" viewBox="0 0 24 24"><path fill="#fff" d="M6.6 10.8c1.4 2.8 3.8 5.1 6.6 6.6l2.2-2.2c.3-.3.7-.4 1-.2 1.1.4 2.3.6 3.6.6.6 0 1 .4 1 1V20c0 .6-.4 1-1 1C10.6 21 3 13.4 3 4c0-.6.4-1 1-1h3.5c.6 0 1 .4 1 1 0 1.3.2 2.5.6 3.6.1.3 0 .7-.2 1L6.6 10.8z"/></svg>
        0800 123 456
      </a>
    </nav>
  </header>

  <h1 class="headline">Free Nationwide<br>Collection &amp; Delivery</h1>
  <p class="subline">with 1500+ garages we collect from home or work</p>

  <form class="quote-form">
    <label class="quote-field"><span class="gb">GB</span>Your registration number</label>
    <label class="quote-field">
      <svg width="10" height="13" viewBox="0 0 10 14"><path fill="#9aa3ad" d="M5 0C2.2 0 0 2.2 0 5c0 3.7 5 9 5 9s5-5.3 5-9c0-2.8-2.2-5-5-5zm0 7a2 2 0 110-4 2 2 0 010 4z"/></svg>
      Your postcode
    </label>
    <button type="button" class="quote-button">GET QUOTE</button>
  </form>
  <a class="reg-help" href="#">* I dont know my registration</a>

  <div class="discount-badge"><span class="small">UP TO</span><span class="big">60%</span><span class="off">OFF</span></div>
  <p class="discount-note">Up to 60 % of main dealer prices</p>

  <section class="hero-links">
    <a class="video-link how"><span class="play"><svg width="8" height="9" viewBox="0 0 8 9"><path fill="#51a0d6" d="M0 0l8 4.5L0 9z"/></svg></span>HOW IT WORKS</a>
    <div class="rating">
      <p class="label">Rated Excellent</p>
      <div class="stars">
        <svg width="9" height="9" viewBox="0 0 24 24"><path fill="#fff" d="M12 2l3 7h7l-5.5 4.5 2 7.5L12 17l-6.5 4 2-7.5L2 9h7z"/></svg>
        <svg width="9" height="9" viewBox="0 0 24 24"><path fill="#fff" d="M12 2l3 7h7l-5.5 4.5 2 7.5L12 17l-6.5 4 2-7.5L2 9h7z"/></svg>
        <svg width="9" height="9" viewBox="0 0 24 24"><path fill="#fff" d="M12 2l3 7h7l-5.5 4.5 2 7.5L12 17l-6.5 4 2-7.5L2 9h7z"/></svg>
        <svg width="9" height="9" viewBox="0 0 24 24"><path fill="#fff" d="M12 2l3 7h7l-5.5 4.5 2 7.5L12 17l-6.5 4 2-7.5L2 9h7z"/></svg>
        <svg width="9" height="9" viewBox="0 0 24 24"><path fill="#fff" d="M12 2l3 7h7l-5.5 4.5 2 7.5L12 17l-6.5 4 2-7.5L2 9h7z"/></svg>
      </div>
      <p class="score">9.8 out of 10 by costumers</p>
      <a class="more">read more</a>
    </div>
    <a class="video-link pitch"><span class="play"><svg width="8" height="9" viewBox="0 0 8 9"><path fill="#51a0d6" d="M0 0l8 4.5L0 9z"/></svg></span>PITCH ROOM</a>
  </section>

  <footer class="press-row">
    <span class="label">As featured on :</span>
    <div class="press-badges">
      <span class="press-badge" style="width:94px"></span>
      <span class="press-badge" style="width:42px;height:14px"></span>
      <span class="press-badge" style="width:40px;height:18px"></span>
      <span class="press-badge" style="width:22px;height:22px"></span>
      <span class="press-badge round"></span>
      <span class="press-badge" style="width:42px;height:14px"></span>
      <span class="press-badge round"></span>
      <span class="press-badge" style="width:32px;height:18px"></span>
      <span class="press-badge" style="width:40px;height:14px"></span>
    </div>
  </footer>
</main>
</body>
</html>
```